I dont have a logo yet. My mind in color is navy blue and khaki maybe a tiny bit of yellow but open to ideas. name of the business is Granite Ridge Builders. Dedicated to all sorts of construction commerical and residential. Im Tomas Vantrell owner of business<br/>Address to business is 862 N. Berrymoor El Paso Tx 79931 <br/>Phone is 9155827143<br/>Id like round corners i also like the see thru card a little.<br/>Open to trademark quotes

Target Market(s)

Construction

Contact Information for Business Card

GRANITE RIDGE BUILDERS LLC

Tomas Vantrell
Director of Operations

Commercial & Residential

9155827143
GRANITE.R.BUILDERS@QUORVANMAIL.COM

Colors
0355a3
fff3d1

Requirements
Must have
• ROUND CORNERS
• BLUE AND KHAKI AND CLEAR
• LOGO

```html
<!DOCTYPE html>
<html lang="en">
<head>
<meta charset="utf-8">
<title>Granite Ridge Builders – Business Card</title>
<link rel="stylesheet" href="https://fonts.googleapis.com/css2?family=Montserrat:wght@500;600;700;800&display=swap">
<style>
  :root {
    --navy: #1b4f8f;
    --navy-deep: #163f75;
    --yellow: #e8cf1a;
    --white: #ffffff;
    --paper: #f1f1f1;
    --stage: #e6e4df;
    --grey-text: #6f7378;
  }
  * { margin: 0; padding: 0; box-sizing: border-box; }
  html, body {
    width: 1200px; height: 780px; overflow: hidden;
    background: var(--stage);
    font-family: "Montserrat", sans-serif;
  }
  .canvas {
    position: relative; width: 1200px; height: 780px;
  }
  .card {
    position: absolute; top: 235px;
    width: 540px; height: 310px;
    border-radius: 22px; overflow: hidden;
    box-shadow: 0 6px 18px rgba(0,0,0,0.18);
  }
  .card-front { left: 40px; background: var(--paper); }
  .card-back {
    left: 620px;
    background: linear-gradient(135deg, var(--navy) 0%, var(--navy-deep) 100%);
    display: flex; align-items: center; justify-content: center;
  }

  /* front layout */
  .front-brand {
    position: absolute; left: 0; top: 0; width: 100%; height: 125px;
    display: flex; align-items: center; justify-content: center; gap: 12px;
  }
  .brand-mark {
    width: 16px; height: 16px; background: var(--navy);
  }
  .brand-name {
    font-weight: 800; font-size: 25px; letter-spacing: 0.5px;
    color: var(--navy); text-transform: uppercase;
  }
  .name-band {
    position: absolute; left: 0; top: 125px; width: 100%; height: 53px;
    background: var(--yellow);
    padding-left: 180px; display: flex; flex-direction: column; justify-content: center;
  }
  .person-name {
    font-weight: 700; font-size: 19px; color: var(--navy);
    text-transform: uppercase; line-height: 1.05;
  }
  .person-role {
    font-weight: 500; font-size: 10px; color: var(--navy);
    text-transform: uppercase; letter-spacing: 0.5px; padding-left: 30px;
  }
  .contact-panel {
    position: absolute; left: 0; top: 178px; width: 100%; height: 132px;
    background: var(--navy);
    padding: 24px 0 0 180px; color: var(--white);
  }
  .contact-phone { font-weight: 700; font-size: 19px; margin-bottom: 6px; }
  .contact-line { font-weight: 500; font-size: 12.5px; line-height: 1.55; }

  /* back layout */
  .back-brand {
    display: flex; align-items: center; gap: 14px;
  }
  .back-brand .brand-mark { background: var(--white); width: 18px; height: 18px; }
  .back-brand .brand-name { color: var(--white); font-size: 28px; }
</style>
</head>
<body>
<main class="canvas">
  <section class="card card-front" aria-label="Business card front">
    <div class="front-brand">
      <span class="brand-mark"></span>
      <span class="brand-name">Granite Ridge Builders</span>
    </div>
    <div class="name-band">
      <p class="person-name">Tomas Vantrell</p>
      <p class="person-role">Owner</p>
    </div>
    <div class="contact-panel">
      <p class="contact-phone">9155827143</p>
      <p class="contact-line">info@quorvanmail.com</p>
      <p class="contact-line">862 N. Berrymoor El Paso Tx 79931</p>
    </div>
  </section>

  <section class="card card-back" aria-label="Business card back">
    <div class="back-brand">
      <span class="brand-mark"></span>
      <span class="brand-name">Granite Ridge Builders</span>
    </div>
  </section>
</main>
</body>
</html>
```